Ridge 9 Ridge Turbine Rentals Pty Ltd

We are a hire company based on the Gold Coast in Australia, we Hire out Generators to construction sites, music festivals, parties, fetes etc. Anywhere where power is required we can provide it.

Ridge 9 Ridge Turbine Rentals pty Ltd also provides all leads, distribution boards, Qualified Electricians to perform all connections. we offer refuelling services and mechanical services. 24Hr on call service - to an actual english speaking operator.

Slogan ''Power Anywhere Anytime"

Industry/Entity Type

Construction

Contact Information for Business Card

M: 0417285963
E: bookings@ridge9ridgeturbinerentals.com.au

```html
<!DOCTYPE html>
<html lang="en">
<head>
<meta charset="utf-8">
<title>Ridge 9 Ridge Turbine Rentals – Business Card</title>
<link rel="stylesheet" href="https://fonts.googleapis.com/css2?family=Open+Sans:wght@400;600;700&display=swap">
<style>
  :root {
    --stage: #e9ebee;
    --sky-top: #a9dde9;
    --sky-mid: #4f93b4;
    --deep-blue: #0f5682;
    --ink: #111417;
    --brand-blue: #1d5f86;
    --band-light: #a6d7e6;
    --white: #ffffff;
  }
  * { box-sizing: border-box; margin: 0; padding: 0; }
  html, body {
    width: 1200px; height: 1000px; overflow: hidden;
    background: var(--stage);
    font-family: "Open Sans", Arial, sans-serif;
  }
  .stage { position: relative; width: 1200px; height: 1000px; }

  .card {
    position: absolute; left: 265px; width: 665px; height: 398px;
    border-radius: 22px; overflow: hidden;
    box-shadow: 0 6px 16px rgba(0,0,0,0.18);
  }

  .brand-name {
    font-weight: 700; line-height: 1.1;
    text-transform: uppercase; white-space: nowrap;
  }
  .brand-name .line-main { display: block; letter-spacing: 1px; }
  .brand-name .line-sub { display: block; text-align: right; letter-spacing: 1px; }

  /* Front */
  .card--front {
    top: 73px;
    background: linear-gradient(180deg, var(--sky-top) 0%, var(--sky-mid) 55%, var(--deep-blue) 100%);
  }
  .front-brand {
    position: absolute; left: 0; right: 0; top: 150px;
    display: flex; justify-content: center; align-items: center; gap: 22px;
  }
  .front-brand .brand-mark {
    width: 90px; height: 90px; border-radius: 50%;
    background: var(--white); opacity: 0.9; flex: none;
  }
  .front-brand .brand-name { color: var(--white); }
  .front-brand .line-main { font-size: 33px; }
  .front-brand .line-sub { font-size: 19px; }
  .tagline {
    position: absolute; left: 0; right: 0; top: 337px;
    text-align: center; color: var(--white); font-size: 16px;
  }

  /* Back */
  .card--back { top: 532px; background: var(--white); }
  .back-brand {
    position: absolute; left: 40px; top: 58px;
    display: flex; align-items: center; gap: 20px;
  }
  .back-brand .brand-mark {
    width: 80px; height: 80px; border-radius: 50%;
    background: var(--brand-blue); flex: none;
  }
  .back-brand .brand-name { color: var(--ink); }
  .back-brand .line-main { font-size: 29px; }
  .back-brand .line-sub { font-size: 16px; }

  .contact {
    position: absolute; right: 38px; top: 200px; text-align: right; color: var(--ink);
  }
  .contact__name { font-size: 20px; font-weight: 600; }
  .contact__role { font-size: 15px; margin-top: 2px; }
  .contact__list { list-style: none; margin-top: 22px; font-size: 15px; }
  .contact__list li { display: flex; justify-content: flex-end; align-items: center; gap: 8px; margin-bottom: 5px; white-space: nowrap; }
  .contact__list svg { width: 16px; height: 14px; fill: var(--brand-blue); flex: none; }

  .base-band { position: absolute; left: 0; right: 0; bottom: 0; height: 48px; display: flex; }
  .base-band__dark { width: 330px; background: linear-gradient(90deg, #2c6d96, #3b7ea6); }
  .base-band__light { flex: 1; background: linear-gradient(90deg, var(--band-light), #3f81a8); }
</style>
</head>
<body>
<main class="stage">
  <section class="card card--front" aria-label="Card front">
    <div class="front-brand">
      <span class="brand-mark" aria-hidden="true"></span>
      <p class="brand-name"><span class="line-main">Ridge 9 Ridge</span><span class="line-sub">Turbine Rentals</span></p>
    </div>
    <p class="tagline">Power Anywhere Anytime</p>
  </section>

  <section class="card card--back" aria-label="Card back">
    <div class="back-brand">
      <span class="brand-mark" aria-hidden="true"></span>
      <p class="brand-name"><span class="line-main">Ridge 9 Ridge</span><span class="line-sub">Turbine Rentals</span></p>
    </div>
    <div class="contact">
      <p class="contact__name">Darren Holt</p>
      <p class="contact__role">Director of Operrations</p>
      <ul class="contact__list">
        <li>0417285963
          <svg viewBox="0 0 16 14" aria-hidden="true"><path d="M1 4c0-2 3-3 7-3s7 1 7 3v1h-4V3.5H5V5H1zM4 6h8l2 3v4H2V9zm4 1.5a2 2 0 1 0 0 4 2 2 0 0 0 0-4z"/></svg>
        </li>
        <li>bookings@ridge9ridgeturbinerentals.com.au
          <svg viewBox="0 0 16 14" aria-hidden="true"><path d="M1 2h14v1L8 8 1 3zm0 2.5 7 5 7-5V12H1z"/></svg>
        </li>
      </ul>
    </div>
    <div class="base-band" aria-hidden="true">
      <div class="base-band__dark"></div>
      <div class="base-band__light"></div>
    </div>
  </section>
</main>
</body>
</html>
```